Business Card - Harlow Birch

Need Business Card design for company named Harlow Birch. Software development focused mainly on Ardel eKallo & oBix Apps. I've attached our logo with both a black and white background. Please add trademark symbol to logo when using.

```html
<!DOCTYPE html>
<html lang="en">
<head>
<meta charset="utf-8">
<title>Harlow Birch — Business Card</title>
<link rel="stylesheet" href="https://fonts.googleapis.com/css2?family=Jost:wght@300;400;600&display=swap">
<style>
  :root {
    --page: #ffffff;
    --card: #2b2b2b;
    --ink: #ffffff;
    --ink-soft: #e6e6e6;
    --amber: #f6b318;
    --orange: #ef7d22;
    --red: #d7262a;
  }
  * { margin: 0; padding: 0; box-sizing: border-box; }
  html, body { width: 1200px; height: 900px; overflow: hidden; background: var(--page); }
  body { position: relative; font-family: "Jost", "Helvetica Neue", Arial, sans-serif; color: var(--ink); }

  .logo-tile {
    position: absolute; left: 36px; top: 70px; width: 114px; height: 114px;
    background: var(--card);
  }
  .card {
    position: absolute; left: 36px; width: 353px; height: 227px;
    background: var(--card);
    box-shadow: 0 2px 4px rgba(0,0,0,0.25);
  }
  .card--front { top: 226px; }
  .card--back { top: 496px; }

  .wordmark { position: absolute; display: flex; flex-direction: column; }
  .wordmark__dot { width: 46px; height: 46px; border-radius: 50%; background: var(--orange); }
  .wordmark__name {
    margin-top: 26px;
    font-weight: 600; font-size: 14px; line-height: 18px; letter-spacing: -0.3px;
    color: var(--ink); white-space: nowrap;
  }
  .logo-tile .wordmark { left: 18px; top: 10px; }
  .card--front .wordmark { left: 18px; top: 16px; }

  .holder {
    position: absolute; left: 24px; top: 98px;
    font-weight: 400; font-size: 16px; line-height: 20px; letter-spacing: 1.4px; color: var(--ink);
  }
  .rule { position: absolute; left: 24px; top: 134px; width: 16px; height: 1px; background: var(--ink); }
  .contact {
    position: absolute; left: 24px; top: 152px;
    font-weight: 400; font-size: 7.5px; line-height: 11px; color: var(--ink-soft); list-style: none;
  }
  .contact__web { margin-top: 9px; }
  .accent {
    position: absolute; left: 17px; top: 209px; width: 17px; height: 2px;
    background: linear-gradient(90deg, var(--amber), var(--orange) 50%, var(--red));
  }
</style>
</head>
<body>
  <div class="logo-tile">
    <div class="wordmark">
      <span class="wordmark__dot"></span>
      <span class="wordmark__name">Harlow Birch</span>
    </div>
  </div>

  <section class="card card--front">
    <div class="wordmark">
      <span class="wordmark__dot"></span>
      <span class="wordmark__name">Harlow Birch ™</span>
    </div>
  </section>

  <section class="card card--back">
    <p class="holder">{Ned Varga}</p>
    <span class="rule"></span>
    <ul class="contact">
      <li>M. +41 555 010203</li>
      <li>ned.varga@harlowbirch.com</li>
      <li class="contact__web">www.harlowbirch.com</li>
    </ul>
    <span class="accent"></span>
  </section>
</body>
</html>
```